Business Card Design Project

Business card design based on the existing logo.

Target Market(s)

Small to medium business owners and CIO's looking for professional IT services.

Industry/Entity Type

Business

Font styles to use
Serif
Sans Serif

Requirements
Must have
• Logo, company name, company details

Text to appear on the business card
Name / Title:
Leon Fairholt
CEO

Address:
Valtiro Limited
Level 3, 42 Kestle St
P O Box 462
Paraparaumu 5391

Other details:
leon@valtiro.co
Ph: 0800 519 308
Mob: +64 21 948 216
www.valtiro.co

Nice to have
• I would look at both single and double sided options. My initial thought is double sided with just the logo with the grey framing for the front and the name and details on the back. But I'm open to other design options.

```html
<!DOCTYPE html>
<html lang="en">
<head>
<meta charset="utf-8">
<title>Valtiro Business Card</title>
<link rel="stylesheet" href="https://fonts.googleapis.com/css2?family=PT+Sans:ital,wght@0,400;0,700;1,700&display=swap">
<style>
  :root {
    --backdrop: #1b1b1b;
    --card: #ffffff;
    --brand-blue: #0066cc;
    --ink-dark: #353535;
    --ink-soft: #6b6b6b;
    --label-text: #ffffff;
  }
  * { box-sizing: border-box; margin: 0; padding: 0; }
  html, body {
    width: 1200px;
    height: 720px;
    overflow: hidden;
    background: var(--backdrop);
    font-family: "PT Sans", sans-serif;
  }
  .sheet { position: relative; width: 1200px; height: 720px; }

  .card {
    position: absolute;
    width: 541px;
    height: 325px;
    background: var(--card);
    overflow: hidden;
  }
  .card--front-a { left: 30px; top: 22px; }
  .card--front-b { left: 628px; top: 22px; }
  .card--back-a { left: 29px; top: 373px; }
  .card--back-b { left: 628px; top: 372px; }

  .card__band {
    position: absolute;
    left: 0; right: 0; bottom: 0;
    height: 32px;
    background: var(--brand-blue);
  }

  .wordmark {
    position: absolute;
    left: 0; right: 0;
    top: 112px;
    display: flex;
    align-items: center;
    justify-content: center;
    gap: 16px;
  }
  .wordmark__mark {
    width: 44px;
    height: 44px;
    background: var(--brand-blue);
  }
  .wordmark__name {
    font-size: 62px;
    font-weight: 400;
    color: var(--ink-dark);
    line-height: 1;
  }

  .identity {
    position: absolute;
    text-align: right;
    color: var(--ink-dark);
    font-weight: 700;
  }
  .identity__name { display: block; }
  .identity__title {
    display: block;
    color: var(--brand-blue);
    font-style: italic;
  }

  .details { position: absolute; }
  .details__label {
    display: inline-block;
    background: var(--brand-blue);
    color: var(--label-text);
    font-weight: 700;
    padding: 0 4px;
  }
  .details__lines {
    list-style: none;
    color: var(--ink-soft);
  }

  /* compact back */
  .card--back-a .identity { right: 274px; top: 18px; }
  .card--back-a .identity__name { font-size: 44px; line-height: 41px; }
  .card--back-a .identity__title { font-size: 27px; line-height: 30px; }
  .card--back-a .details { left: 291px; }
  .card--back-a .details--address { top: 27px; }
  .card--back-a .details--other { top: 161px; }
  .card--back-a .details__label { font-size: 18px; line-height: 22px; }
  .card--back-a .details__lines { font-size: 15px; line-height: 19.5px; margin-top: 4px; }

  /* large-name back */
  .card--back-b .identity { right: 284px; top: 46px; }
  .card--back-b .identity__name { font-size: 66px; line-height: 60px; }
  .card--back-b .identity__title { font-size: 34px; line-height: 40px; margin-top: 8px; }
  .card--back-b .details { left: 302px; }
  .card--back-b .details--address { top: 30px; }
  .card--back-b .details--other { top: 165px; }
  .card--back-b .details__label { font-size: 18px; line-height: 23px; }
  .card--back-b .details__lines { font-size: 15.5px; line-height: 19.5px; margin-top: 5px; }
</style>
</head>
<body>
<main class="sheet">
  <section class="card card--front-a" aria-label="Card front">
    <div class="wordmark">
      <span class="wordmark__mark"></span>
      <span class="wordmark__name">Valtiro</span>
    </div>
    <div class="card__band"></div>
  </section>

  <section class="card card--front-b" aria-label="Card front, alternative">
    <div class="wordmark">
      <span class="wordmark__mark"></span>
      <span class="wordmark__name">Valtiro</span>
    </div>
    <div class="card__band"></div>
  </section>

  <section class="card card--back-a" aria-label="Card back">
    <div class="identity">
      <span class="identity__name">Leon<br>Fairholt</span>
      <span class="identity__title">CEO</span>
    </div>
    <div class="details details--address">
      <span class="details__label">Address</span>
      <ul class="details__lines">
        <li>Valtiro Limited</li>
        <li>Level 3, 42 Kestle St</li>
        <li>P O Box 462</li>
        <li>Paraparaumu 5391</li>
      </ul>
    </div>
    <div class="details details--other">
      <span class="details__label">Other details</span>
      <ul class="details__lines">
        <li>leon@valtiro.co</li>
        <li>Ph: 0800 519 308</li>
        <li>Mob: +64 21 948 216</li>
        <li>www.valtiro.co</li>
      </ul>
    </div>
    <div class="card__band"></div>
  </section>

  <section class="card card--back-b" aria-label="Card back, alternative">
    <div class="identity">
      <span class="identity__name">Leon<br>Fairholt</span>
      <span class="identity__title">CEO</span>
    </div>
    <div class="details details--address">
      <span class="details__label">Address</span>
      <ul class="details__lines">
        <li>Valtiro Limited</li>
        <li>Level 3, 42 Kestle St</li>
        <li>P O Box 462</li>
        <li>Paraparaumu 5391</li>
      </ul>
    </div>
    <div class="details details--other">
      <span class="details__label">Other details</span>
      <ul class="details__lines">
        <li>leon@valtiro.co</li>
        <li>Ph: 0800 519 308</li>
        <li>Mob: +64 21 948 216</li>
        <li>www.valtiro.co</li>
      </ul>
    </div>
    <div class="card__band"></div>
  </section>
</main>
</body>
</html>
```